Brochure Design

We need a 6 page Brochure designed for our product, please see attached document for more information. The content should focus on account work.

Target Market(s)

Businesses that use a taxi service for their business

Requirements
Must have
• Must have key content on the services we provide for Account work

```html
<!DOCTYPE html>
<html lang="en">
<head>
<meta charset="utf-8">
<title>Ridova – Business Account Brochure</title>
<link rel="stylesheet" href="https://fonts.googleapis.com/css2?family=Open+Sans:ital,wght@0,400;0,600;0,700;0,800;1,400&display=swap">
<style>
  :root{
    --stage:#d3d3d3;
    --orange:#f4a81d;
    --orange-deep:#e8960c;
    --ink:#141414;
    --charcoal:#242424;
    --slate:#555;
    --mist:#ececec;
    --paper:#f7f7f7;
    --white:#fff;
    --muted:#6d6d6d;
  }
  *{box-sizing:border-box;margin:0;padding:0}
  html,body{width:898px;height:1200px;overflow:hidden}
  body{background:var(--stage);font-family:"Open Sans",Arial,sans-serif;position:relative;color:var(--ink)}
  .spread{position:absolute;left:29px;width:840px;height:280px;display:flex;box-shadow:0 6px 18px rgba(0,0,0,.18)}
  .spread--outside{top:230px}
  .spread--inside{top:690px}
  .panel{position:relative;width:280px;height:280px;overflow:hidden}

  /* shared */
  .photo{position:absolute;display:block}
  .hex{clip-path:polygon(25% 0,75% 0,100% 50%,75% 100%,25% 100%,0 50%)}
  .brand{display:flex;align-items:center;gap:6px;font-weight:800;color:var(--ink);letter-spacing:-.5px}
  .brand__dot{display:block;border-radius:50%;background:var(--ink)}
  .web{font-weight:700;letter-spacing:.3px}

  /* outside: app panel */
  .panel--app{background:var(--paper)}
  .panel--app .phones{left:14px;top:14px;width:122px;height:152px;border-radius:10px;background:linear-gradient(160deg,#2a2a2a 0%,#f6d24a 35%,#e9ecef 60%,#2a2a2a 100%)}
  .panel--app .backdrop{position:absolute;left:125px;top:0;width:155px;height:235px;background:var(--charcoal);clip-path:polygon(18% 0,100% 0,100% 100%,0 100%)}
  .panel--app .portrait{left:128px;top:6px;width:150px;height:150px;background:radial-gradient(circle at 50% 45%,#d9b08c 0%,#9a7a60 45%,#5d5d5d 100%)}
  .app-cta{position:absolute;left:14px;top:180px;font-size:7.4px;font-weight:800;color:var(--orange);text-transform:uppercase}
  .band{position:absolute;left:0;bottom:0;width:100%;height:45px;background:var(--ink)}
  .stores{position:absolute;left:12px;bottom:12px;display:flex;gap:7px}
  .store{width:52px;height:20px;border-radius:4px;background:#000;border:1px solid #8a8a8a}
  .store--wide{width:60px}
  .panel--app .web{position:absolute;left:140px;bottom:16px;font-size:10px;color:var(--orange)}

  /* outside: back cover */
  .panel--back{background:linear-gradient(180deg,#1d1d1d,#0d0d0d 60%,#050505);color:var(--white);text-align:center}
  .panel--back .brand{position:absolute;left:50%;top:30px;transform:translateX(-50%);color:var(--orange);font-size:30px}
  .panel--back .brand__dot{width:30px;height:30px;background:var(--orange)}
  .features{position:absolute;left:14px;top:100px;list-style:none;text-align:left}
  .features li{display:flex;align-items:center;gap:6px;font-size:6.6px;margin-bottom:8.5px;color:#e6e6e6}
  .bullet{width:7px;height:7px;border-radius:50%;background:var(--orange);flex:none;position:relative}
  .bullet::after{content:"";position:absolute;left:2px;top:2.2px;width:2.5px;height:2.5px;border-top:1px solid var(--ink);border-right:1px solid var(--ink);transform:rotate(45deg)}
  .contact-pill{position:absolute;left:50%;top:168px;transform:translateX(-50%);width:118px;height:16px;border-radius:8px;background:linear-gradient(180deg,#ffc23a,var(--orange-deep));font-size:9px;font-weight:800;line-height:16px;color:var(--white)}
  .panel--back .tagline{position:absolute;left:0;right:0;top:196px;font-size:6.4px;color:#cfcfcf;text-transform:uppercase}
  .panel--back .web{position:absolute;left:0;right:0;top:207px;font-size:11px;color:var(--orange)}
  .panel--back .band{background:#000}

  /* outside: front cover */
  .panel--cover{background:var(--mist)}
  .cover-shade{position:absolute;inset:0}
  .cover-title{position:absolute;right:10px;top:10px;text-align:right;font-size:8.6px;line-height:1.25;color:var(--orange);text-transform:uppercase}
  .panel--cover .portrait{left:6px;top:22px;width:190px;height:180px;background:radial-gradient(circle at 45% 40%,#c99a78 0%,#7a5a48 40%,#3f6f5e 75%,#9fa3a6 100%)}
  .badge{position:absolute;left:128px;top:72px;width:122px;height:112px;background:var(--orange);display:flex;flex-direction:column;align-items:center;justify-content:center;gap:6px}
  .badge .brand{font-size:22px}
  .badge .brand__dot{width:16px;height:16px}
  .badge__line{font-size:6.6px;line-height:1.25;text-align:center;color:var(--ink);text-transform:uppercase}
  .panel--cover .web{position:absolute;right:10px;bottom:10px;font-size:8.6px;color:var(--ink)}

  /* inside: intro */
  .panel--intro{background:var(--mist);padding:22px 18px 0 20px}
  .intro-title{font-size:9.4px;line-height:1.2;color:var(--orange);text-transform:uppercase;font-weight:400;margin-bottom:10px}
  .panel--intro p{font-size:5.8px;line-height:1.55;color:var(--slate);margin-bottom:7px}
  .taxi-strip{position:absolute;left:0;right:0;bottom:0;height:15px;background:linear-gradient(180deg,var(--orange),var(--orange-deep))}

  /* inside: services */
  .panel--services{background:linear-gradient(180deg,#262626,#171717)}
  .services-tab{position:absolute;left:70px;top:0;width:140px;height:70px;background:var(--orange);clip-path:polygon(0 0,100% 0,100% 70%,50% 100%,0 70%);display:flex;align-items:center;justify-content:center;padding-bottom:14px}
  .services-tab .brand{font-size:18px}
  .services-tab .brand__dot{width:14px;height:14px}
  .services{position:absolute;left:18px;top:88px;list-style:none}
  .services li{display:flex;align-items:center;gap:6px;font-size:6.4px;color:#ececec;margin-bottom:5.4px}
  .services-web{position:absolute;left:50%;bottom:14px;transform:translateX(-50%);background:#0a0a0a;padding:3px 12px;font-size:10px;color:var(--orange)}

  /* inside: benefits */
  .panel--benefits{background:var(--white)}
  .panel--benefits .lifestyle{right:0;top:0;width:150px;height:88px;background:linear-gradient(135deg,#cfd8e0,#8fa2b3 50%,#e0b25a);clip-path:polygon(22% 0,100% 0,100% 100%,0 100%)}
  .panel--benefits .app-screen{left:190px;top:98px;width:52px;height:100px;border-radius:7px;background:linear-gradient(180deg,#1c1c1c 0 8%,#f8c53a 8% 88%,#1c1c1c 88%)}
  .benefits-lead{position:absolute;left:16px;top:42px;width:120px;font-size:6.4px;line-height:1.4;color:var(--slate)}
  .benefit{position:absolute;left:14px;width:170px;display:flex;gap:7px;align-items:flex-start}
  .benefit__icon{width:20px;height:20px;border-radius:50%;border:1.5px solid var(--orange);flex:none;display:flex;align-items:center;justify-content:center}
  .benefit__title{font-size:6.6px;font-weight:800;color:var(--orange);text-transform:uppercase}
  .benefit__text{font-size:5.2px;line-height:1.4;color:var(--muted);width:110px}
</style>
</head>
<body>

<section class="spread spread--outside" aria-label="Brochure outside spread">
  <article class="panel panel--app">
    <div class="photo phones" role="img" aria-label="Two smartphones showing the booking app with a map"></div>
    <div class="backdrop"></div>
    <div class="photo portrait hex" role="img" aria-label="Smiling businessman looking at his phone"></div>
    <p class="app-cta">Download the Ridova app from your smartphone today!</p>
    <div class="band">
      <div class="stores">
        <span class="store" role="img" aria-label="App store badge"></span>
        <span class="store store--wide" role="img" aria-label="App store badge"></span>
      </div>
      <span class="web">www.ridova.cab</span>
    </div>
  </article>

  <article class="panel panel--back">
    <div class="brand"><span class="brand__dot"></span>ridova</div>
    <ul class="features">
      <li><span class="bullet"></span>Call a taxi any time, any place</li>
      <li><span class="bullet"></span>The Driver accept and you receive the Taxi details</li>
      <li><span class="bullet"></span>Watch your Taxi on its way, jump in and go to your destination</li>
      <li><span class="bullet"></span>Best experience with Ridova App</li>
    </ul>
    <div class="contact-pill">CONTACT US</div>
    <p class="tagline">Your safety is our priority</p>
    <p class="web">www.ridova.cab</p>
    <div class="band" style="height:24px"></div>
  </article>

  <article class="panel panel--cover">
    <svg class="cover-shade" width="280" height="280" viewBox="0 0 280 280" aria-hidden="true">
      <polygon points="0,0 120,0 0,90" fill="#3a3a3a"/>
      <polygon points="0,200 0,280 200,280 150,220" fill="#4a4a4a"/>
      <polygon points="150,0 200,0 230,60 205,60" fill="#bdbdbd"/>
    </svg>
    <p class="cover-title">Exceptional travel for<br>a modern business</p>
    <div class="photo portrait hex" role="img" aria-label="Smiling businesswoman talking on her phone"></div>
    <div class="badge hex">
      <div class="brand"><span class="brand__dot"></span>ridova</div>
      <p class="badge__line">Your safety<br>is our priority</p>
    </div>
    <p class="web">www.ridova.cab</p>
  </article>
</section>

<section class="spread spread--inside" aria-label="Brochure inside spread">
  <article class="panel panel--intro">
    <h2 class="intro-title">Exceptional travel for<br>a modern business</h2>
    <p>Your business can't wait, but it shouldn't compromise on quality. As the Business Account provider, we move executives across London with set fares and phone bookings in every vehicle, so you can stay focused on your business every step of your journey.</p>
    <p>Take full control of your business travel with the Ridova Portal, which helps you manage bookings, users and invoices in one place. Plus, with a dedicated account manager, you'll have access to 24/7 support should you need it.</p>
    <p>Open a business account today and take advantage of our executive services outside of London, whether your business travel takes you across the London, Europe, UAE or Asia.</p>
    <div class="taxi-strip"></div>
  </article>

  <article class="panel panel--services">
    <div class="services-tab"><div class="brand"><span class="brand__dot"></span>ridova</div></div>
    <ul class="services">
      <li><span class="bullet"></span>Cost effective service with quality vehicles</li>
      <li><span class="bullet"></span>Dedicated service via online system</li>
      <li><span class="bullet"></span>Bookings can be made quickly and simple</li>
      <li><span class="bullet"></span>Phone support when needed 24/7</li>
      <li><span class="bullet"></span>Advanced booking control</li>
      <li><span class="bullet"></span>Regular report scheduled booking options</li>
      <li><span class="bullet"></span>Airport Transfer</li>
      <li><span class="bullet"></span>Mid-range to Executive vehicles</li>
      <li><span class="bullet"></span>Your entry point to the UK-wide Ridova network</li>
    </ul>
    <p class="services-web web">www.ridova.cab</p>
  </article>

  <article class="panel panel--benefits">
    <div class="photo lifestyle" role="img" aria-label="Business traveller holding a smartphone"></div>
    <div class="photo app-screen" role="img" aria-label="Smartphone showing the booking app screen"></div>
    <p class="benefits-lead">Ridova has been the second largest taxi hailing company in Europe for the last 3 years.</p>
    <div class="benefit" style="top:112px">
      <span class="benefit__icon"><svg width="10" height="10" viewBox="0 0 24 24"><path d="M6.6 10.8a15 15 0 006.6 6.6l2.2-2.2a1 1 0 011-.25 11.4 11.4 0 003.6.6 1 1 0 011 1V20a1 1 0 01-1 1A17 17 0 013 4a1 1 0 011-1h3.5a1 1 0 011 1c0 1.25.2 2.45.6 3.6a1 1 0 01-.25 1z" fill="#f4a81d"/></svg></span>
      <div><p class="benefit__title">24/7 Support</p><p class="benefit__text">Our Business Management Team and support are available all hours of every day.</p></div>
    </div>
    <div class="benefit" style="top:150px">
      <span class="benefit__icon"><svg width="10" height="10" viewBox="0 0 24 24"><path d="M12 2a7 7 0 00-7 7c0 5 7 13 7 13s7-8 7-13a7 7 0 00-7-7zm0 9.5A2.5 2.5 0 1112 6.5a2.5 2.5 0 010 5z" fill="#f4a81d"/></svg></span>
      <div><p class="benefit__title">Average 7 min pick ups</p><p class="benefit__text">Benefit from a prompt service, ensuring you're never kept waiting long.</p></div>
    </div>
    <div class="benefit" style="top:188px">
      <span class="benefit__icon"><svg width="10" height="10" viewBox="0 0 24 24"><path d="M4 12l5 5L20 6" stroke="#f4a81d" stroke-width="3" fill="none"/></svg></span>
      <div><p class="benefit__title">Trained, hand picked drivers</p><p class="benefit__text">Our drivers are trained and vetted to ensure top service, security and safety.</p></div>
    </div>
    <div class="taxi-strip"></div>
  </article>
</section>

</body>
</html>
```